We need a letterhead incorporating our logo (uploaded file), with the name of our organization (Dunmore Hollis County Police Association) and our slogan (Strength in Unity). Dark blue should be incorporated somewhere in the design, either the font color or elsewhere. Please make sure our logo is included in the design. The organization is a law enforcement union type group.

Target Market(s)

Members of our association, policticians, and anyone receiving our letters

Colors
0255a3

Requirements
Must have
• Our logo, Association name, and slogan.
Nice to have
• A professional and eye-catching letterhead design incorporating the logo, name, and slogan.

```html
<!DOCTYPE html>
<html lang="en">
<head>
<meta charset="utf-8">
<title>Dunmore Hollis County Police Association — Letterhead</title>
<link rel="stylesheet" href="https://fonts.googleapis.com/css2?family=Libre+Baskerville:wght@700&family=Montserrat:wght@500;700&display=swap">
<style>
  :root {
    --navy: #03206b;
    --brand-blue: #0255a3;
    --royal: #0b4fc7;
    --title-blue: #1b3f8f;
    --teal: #3ccfd2;
    --aqua: #6cf1f3;
    --ink: #111111;
    --paper: #ffffff;
    --faint-ring: #eef1fb;
  }
  * { margin: 0; padding: 0; box-sizing: border-box; }
  html, body { width: 849px; height: 1200px; overflow: hidden; background: var(--paper); }
  .letterhead { position: relative; width: 849px; height: 1200px; background: var(--paper); overflow: hidden; }

  .top-band {
    position: absolute; left: 0; top: 0; width: 849px; height: 18px;
    background: linear-gradient(90deg, var(--aqua) 0%, var(--teal) 30%, var(--royal) 65%, var(--navy) 100%);
  }

  .brand-mark {
    position: absolute; left: 48px; top: 108px; width: 112px; height: 112px;
    border-radius: 50%; border: 5px solid var(--brand-blue);
    display: flex; align-items: center; justify-content: center;
    font-family: "Libre Baskerville", Georgia, serif; font-weight: 700;
    font-size: 17px; color: var(--brand-blue); letter-spacing: 0.5px;
  }

  .identity { position: absolute; left: 178px; top: 133px; }
  .identity .org-name {
    font-family: "Libre Baskerville", Georgia, serif; font-weight: 700;
    font-size: 15.5px; line-height: 18px; color: var(--title-blue);
    text-transform: uppercase; letter-spacing: 0.4px;
  }
  .identity .slogan {
    margin-top: 8px;
    font-family: "Montserrat", Arial, sans-serif; font-weight: 500;
    font-size: 15.5px; color: var(--ink);
  }

  .contact { position: absolute; right: 38px; top: 112px; list-style: none; }
  .contact li {
    display: flex; align-items: center; justify-content: flex-end;
    height: 26px; margin-bottom: 1.7px;
    font-family: "Montserrat", Arial, sans-serif; font-weight: 500;
    font-size: 15.5px; color: var(--ink);
  }
  .contact li.phone { font-weight: 700; font-size: 20px; }
  .contact .icon {
    width: 26px; height: 26px; border-radius: 4px; margin-left: 6px;
    display: flex; align-items: center; justify-content: center; flex: none;
  }
  .icon.phone-icon { background: var(--navy); }
  .icon.mail-icon { background: var(--royal); }
  .icon.web-icon { background: var(--teal); }
  .icon.pin-icon { background: var(--aqua); }

  .watermark { position: absolute; left: 199px; top: 370px; width: 440px; height: 440px; }

  .bottom-band { position: absolute; left: 0; top: 1152px; width: 849px; height: 48px; }
</style>
</head>
<body>
<div class="letterhead">
  <div class="top-band"></div>

  <div class="brand-mark">DHCPA</div>

  <div class="identity">
    <div class="org-name">Dunmore Hollis County<br>Police Association</div>
    <div class="slogan">Strength in Unity</div>
  </div>

  <ul class="contact">
    <li class="phone">0123456789
      <span class="icon phone-icon">
        <svg width="14" height="14" viewBox="0 0 24 24" fill="none" stroke="#fff" stroke-width="2.2" stroke-linecap="round" stroke-linejoin="round"><path d="M22 16.9v3a2 2 0 0 1-2.2 2 19.8 19.8 0 0 1-8.6-3.1 19.5 19.5 0 0 1-6-6A19.8 19.8 0 0 1 2.1 4.2 2 2 0 0 1 4.1 2h3a2 2 0 0 1 2 1.7c.1.9.4 1.9.7 2.8a2 2 0 0 1-.5 2.1L8 9.8a16 16 0 0 0 6 6l1.3-1.3a2 2 0 0 1 2.1-.4c.9.3 1.8.6 2.8.7a2 2 0 0 1 1.7 2z"/></svg>
      </span>
    </li>
    <li>info@dhcpa.org
      <span class="icon mail-icon">
        <svg width="15" height="12" viewBox="0 0 24 18" fill="none" stroke="#fff" stroke-width="2"><rect x="1" y="1" width="22" height="16" rx="1"/><path d="M1 1l11 9 11-9M1 17l8-7M23 17l-8-7"/></svg>
      </span>
    </li>
    <li>www.dhcpa.org
      <span class="icon web-icon">
        <svg width="15" height="15" viewBox="0 0 24 24" fill="none" stroke="#fff" stroke-width="2"><circle cx="12" cy="12" r="10"/><path d="M2 12h20M12 2c3 3 3 17 0 20M12 2c-3 3-3 17 0 20"/></svg>
      </span>
    </li>
    <li>Lorem ipsum dolor sit amet
      <span class="icon pin-icon">
        <svg width="12" height="15" viewBox="0 0 20 26" fill="#fff"><path d="M10 0a9 9 0 0 0-9 9c0 7 9 17 9 17s9-10 9-17a9 9 0 0 0-9-9zm0 12.5A3.5 3.5 0 1 1 10 5.5a3.5 3.5 0 0 1 0 7z"/></svg>
      </span>
    </li>
  </ul>

  <svg class="watermark" viewBox="0 0 440 440" aria-hidden="true">
    <circle cx="220" cy="220" r="208" fill="none" stroke="var(--faint-ring)" stroke-width="24"/>
  </svg>

  <svg class="bottom-band" viewBox="0 0 849 48" preserveAspectRatio="none" aria-hidden="true">
    <defs>
      <linearGradient id="band-fade" x1="0" y1="0" x2="1" y2="0">
        <stop offset="0" stop-color="#0a3fc4"/>
        <stop offset="0.5" stop-color="#2aa9d6"/>
        <stop offset="1" stop-color="#6cf6f6"/>
      </linearGradient>
    </defs>
    <polygon points="0,0 283,0 296,48 0,48" fill="var(--navy)"/>
    <polygon points="292,0 312,0 325,48 305,48" fill="var(--navy)"/>
    <polygon points="320,0 849,0 849,48 333,48" fill="url(#band-fade)"/>
  </svg>
</div>
</body>
</html>
```